Birchwood Clover Business Cards

I need a business card with my logo, number, Facebook account, and some information about what I am selling. Green card with logo on the front. 555-218-3946 phone number, @birchwoodclover Facebook, •Orchardgrass Hay •Alfalfa Hay •Mixed Grass Hay , and “Premium Quality Hay” all written on the back.

Target Market(s)

Hay

Contact Information for Business Card

Phone number, Facebook, different types of hay.

Colors
00AB8E
00BBA5
67D7C9
C6EFE9
E9F9F6

```html
<!DOCTYPE html>
<html lang="en">
<head>
<meta charset="utf-8">
<title>Birchwood Clover Business Cards</title>
<link rel="stylesheet" href="https://fonts.googleapis.com/css2?family=Arimo:wght@400;700&display=swap">
<style>
  :root {
    --stage: #c9c9c9;
    --stage-dark: #a9a9a9;
    --card: #242424;
    --card-edge: #00a651;
    --brand-green: #00a651;
    --rule-grey: #6a6a6a;
    --ink: #ffffff;
  }
  * { box-sizing: border-box; margin: 0; padding: 0; }
  html, body { width: 1200px; height: 800px; overflow: hidden; }
  body {
    background: linear-gradient(135deg, var(--stage-dark), var(--stage) 60%, #d6d6d6);
    font-family: "Arimo", Arial, sans-serif;
    color: var(--ink);
    position: relative;
  }
  .card {
    position: absolute;
    top: 240px;
    width: 540px;
    height: 310px;
    background: var(--card);
    border-bottom: 3px solid var(--card-edge);
    box-shadow: 0 14px 30px rgba(0,0,0,.35);
  }
  .card--back { left: 45px; }
  .card--front { left: 615px; }

  /* brand lockup */
  .brand { display: flex; align-items: center; gap: 12px; }
  .brand__dot { width: 30px; height: 30px; border-radius: 50%; background: var(--brand-green); flex: none; }
  .brand__name { font-weight: 700; font-size: 30px; color: var(--ink); white-space: nowrap; }

  /* back side */
  .back__header {
    position: absolute; left: 40px; top: 52px; right: 40px;
    display: flex; align-items: center; gap: 22px;
  }
  .back__divider { width: 1px; height: 56px; background: var(--rule-grey); }
  .back__rule {
    position: absolute; left: 40px; right: 40px; top: 156px;
    height: 1px; background: var(--brand-green);
  }
  .contacts {
    position: absolute; left: 40px; top: 126px;
    display: flex; gap: 60px; font-size: 15px; transform: translateY(-50%);
  }
  .contact { display: flex; align-items: center; gap: 10px; }
  .contact__icon {
    width: 26px; height: 26px; border-radius: 50%;
    background: var(--brand-green); display: grid; place-items: center;
  }
  .offer-list {
    position: absolute; left: 40px; top: 184px; right: 40px;
    list-style: none;
    display: grid; grid-template-columns: 1fr 1fr; row-gap: 14px; column-gap: 20px;
    font-size: 16px;
  }
  .offer-list li { display: flex; align-items: center; gap: 9px; }
  .offer-list li::before {
    content: ""; width: 9px; height: 9px; border-radius: 50%; background: var(--brand-green);
  }

  /* front side */
  .front__lockup {
    position: absolute; left: 50%; top: 50%; transform: translate(-50%, -50%);
    display: flex; flex-direction: column; align-items: center; gap: 14px;
  }
  .front__lockup .brand__dot { width: 40px; height: 40px; }
  .front__lockup .brand__name { font-size: 34px; }
  .front__phone { font-weight: 700; font-size: 40px; letter-spacing: 1px; }
</style>
</head>
<body>
  <section class="card card--back" aria-label="Card back">
    <header class="back__header">
      <div class="brand">
        <span class="brand__dot"></span>
        <span class="brand__name">Birchwood Clover</span>
      </div>
    </header>
    <div class="contacts">
      <div class="contact">
        <span class="contact__icon">
          <svg width="14" height="14" viewBox="0 0 24 24" aria-hidden="true">
            <path fill="#fff" d="M6.6 10.8a15.1 15.1 0 0 0 6.6 6.6l2.2-2.2c.3-.3.7-.4 1-.2 1.1.4 2.3.6 3.6.6.6 0 1 .4 1 1V20c0 .6-.4 1-1 1A17 17 0 0 1 3 4c0-.6.4-1 1-1h3.5c.6 0 1 .4 1 1 0 1.3.2 2.5.6 3.6.1.3 0 .7-.2 1z"/>
          </svg>
        </span>
        <span>555-218-3946</span>
      </div>
      <div class="contact">
        <span class="contact__icon"></span>
        <span>@birchwoodclover</span>
      </div>
    </div>
    <div class="back__rule"></div>
    <ul class="offer-list">
      <li>Orchardgrass Hay</li>
      <li>Alfalfa Hay</li>
      <li>Mixed Grass Hay</li>
      <li>Premium Quality Hay</li>
    </ul>
  </section>

  <section class="card card--front" aria-label="Card front">
    <div class="front__lockup">
      <div class="brand">
        <span class="brand__dot"></span>
        <span class="brand__name">Birchwood Clover</span>
      </div>
      <div class="front__phone">555-218-3946</div>
    </div>
  </section>
</body>
</html>
```